Kestrel Aid Services Banner Ad

Need a 750 x 250-pixel banner ad with the company Logo included. Please see company website at www.kestrelaidservices.com for more information.

```html
<!DOCTYPE html>
<html lang="en">
<head>
<meta charset="utf-8">
<title>Kestrel Aid Services – Support Coordination Banner</title>
<link href="https://fonts.googleapis.com/css2?family=Oswald:wght@500;600&display=swap" rel="stylesheet">
<style>
  :root {
    --navy: #1c4d78;
    --navy-deep: #163f63;
    --green: #6cc024;
    --green-dark: #58a51a;
    --white: #ffffff;
    --sky-top: #cfe0ec;
    --sky-low: #e6eef2;
    --water: #5f8ea9;
    --water-deep: #3f6f8c;
  }
  html, body {
    margin: 0;
    padding: 0;
    overflow: hidden;
    background: #ffffff;
  }
  .banner {
    position: relative;
    width: 1200px;
    height: 400px;
    overflow: hidden;
    font-family: "Oswald", "Arial Narrow", sans-serif;
  }
  .banner__scene {
    position: absolute;
    inset: 0;
    background: linear-gradient(180deg,
      var(--sky-top) 0%,
      var(--sky-low) 52%,
      var(--water) 58%,
      var(--water-deep) 100%);
  }
  .banner__shapes {
    position: absolute;
    inset: 0;
  }
  .brand {
    position: absolute;
    top: 60px;
    left: 400px;
    transform: translateX(-50%);
    display: flex;
    align-items: center;
    gap: 14px;
    color: var(--white);
    white-space: nowrap;
  }
  .brand__dot {
    width: 34px;
    height: 34px;
    border-radius: 50%;
    background: var(--white);
  }
  .brand__name {
    font-weight: 600;
    font-size: 40px;
    letter-spacing: 1px;
    line-height: 1;
    text-transform: uppercase;
  }
  .headline {
    position: absolute;
    top: 140px;
    left: 400px;
    transform: translateX(-50%);
    margin: 0;
    color: var(--white);
    font-weight: 600;
    font-size: 50px;
    line-height: 58px;
    text-align: center;
    text-transform: uppercase;
    white-space: nowrap;
  }
  .cta {
    position: absolute;
    top: 293px;
    left: 275px;
    width: 213px;
    height: 54px;
    border-radius: 27px;
    background: linear-gradient(180deg, var(--green) 0%, var(--green-dark) 100%);
    color: var(--white);
    font-weight: 500;
    font-size: 20px;
    line-height: 54px;
    text-align: center;
    text-transform: uppercase;
    text-decoration: none;
  }
</style>
</head>
<body>
  <div class="banner">
    <div class="banner__scene" role="img" aria-label="Photo of a young man in a wheelchair on a wooden jetty, arms resting on the posts, looking out over calm open water under a pale sky"></div>

    <svg class="banner__shapes" width="1200" height="400" viewBox="0 0 1200 400" aria-hidden="true">
      <polygon class="panel-accent" points="0,0 722,0 602,400 0,400" fill="var(--green)"/>
      <polygon class="panel" points="0,0 696,0 576,400 0,400" fill="var(--navy)"/>
      <polygon class="panel-edge" points="0,0 22,0 0,34" fill="var(--green)"/>
    </svg>

    <div class="brand">
      <span class="brand__dot"></span>
      <span class="brand__name">Kestrel Aid Services</span>
    </div>

    <h1 class="headline">Support Coordination<br>Across New Jersey</h1>

    <a class="cta" href="#">Read More</a>
  </div>
</body>
</html>
```